Young and modern Electrical company working in the commercial arena.

Wanting a business card design thats modern and will last. Maybe Minimalist? Happy to look at changing my logo

Target Market(s)

Builders, Project Managers

Industry/Entity Type

Electrical

Contact Information for Business Card

Name
Address
Phone number
Job title

Logo Text

our name or just the logo i'm open to ideas

Font styles to use
Sans Serif

Requirements
Nice to have
• would like to keep the purple in our current logo. it's kinda unique to our market
Should not have
• Don't want it to be to busy. simple is best i think

```html
<!DOCTYPE html>
<html lang="en">
<head>
<meta charset="utf-8">
<title>Voltmere Electrical – Business Card</title>
<link href="https://fonts.googleapis.com/css2?family=Exo+2:wght@400;500&family=Open+Sans:wght@400;600&display=swap" rel="stylesheet">
<style>
  :root {
    --purple: #6a3aa8;
    --purple-deep: #512a8a;
    --ink: #111111;
    --paper: #f6f6f7;
    --paper-shade: #e9e9ec;
    --backdrop: #d9d6d2;
    --text-dark: #1d1d1f;
  }
  * { box-sizing: border-box; margin: 0; padding: 0; }
  html, body { width: 1200px; height: 780px; overflow: hidden; }
  body {
    background: var(--backdrop);
    display: flex;
    align-items: center;
    justify-content: center;
    gap: 40px;
    font-family: "Open Sans", Arial, sans-serif;
  }
  .card {
    position: relative;
    width: 520px;
    height: 300px;
    border-radius: 16px;
    overflow: hidden;
    background: linear-gradient(160deg, var(--paper), var(--paper-shade));
    box-shadow: 0 6px 18px rgba(0,0,0,0.18);
  }
  .card-bands { position: absolute; inset: 0; width: 100%; height: 100%; }
  .wordmark {
    font-family: "Exo 2", Arial, sans-serif;
    font-weight: 500;
    color: var(--purple);
    letter-spacing: 2px;
    white-space: nowrap;
  }
  /* front */
  .card-front .wordmark {
    position: absolute;
    top: 50%; left: 50%;
    transform: translate(-50%, -50%);
    font-size: 36px;
  }
  /* back */
  .card-back .wordmark {
    position: absolute;
    top: 30px; right: 34px;
    font-size: 26px;
  }
  .contact {
    position: absolute;
    top: 80px; left: 34px;
    color: var(--text-dark);
  }
  .contact-name {
    font-family: "Exo 2", Arial, sans-serif;
    font-size: 17px;
    font-weight: 500;
    color: var(--purple);
  }
  .contact-title { font-size: 11px; margin-bottom: 10px; }
  .contact-list { list-style: none; font-size: 11px; }
  .contact-list li { display: flex; align-items: center; gap: 7px; margin-bottom: 4px; }
  .contact-icon { width: 14px; height: 14px; flex: none; }
  .address {
    position: absolute;
    left: 0; right: 0; bottom: 13px;
    text-align: center;
    color: #fff;
    font-size: 11px;
    letter-spacing: 0.5px;
  }
</style>
</head>
<body>

  <section class="card card-front" aria-label="Business card front">
    <svg class="card-bands" viewBox="0 0 520 300" preserveAspectRatio="none" aria-hidden="true">
      <path d="M0 0 H520 V52 Q260 92 0 52 Z" fill="var(--purple)"/>
      <path d="M0 52 Q260 92 520 52 V60 Q300 112 0 80 Z" fill="var(--ink)"/>
      <path d="M0 300 H520 V248 Q260 208 0 248 Z" fill="var(--purple)"/>
      <path d="M520 248 Q260 208 0 248 V240 Q220 188 520 220 Z" fill="var(--ink)"/>
    </svg>
    <div class="wordmark">voltmere electrical</div>
  </section>

  <section class="card card-back" aria-label="Business card back">
    <svg class="card-bands" viewBox="0 0 520 300" preserveAspectRatio="none" aria-hidden="true">
      <path d="M0 300 H520 V264 Q300 252 0 240 Z" fill="var(--purple)"/>
      <path d="M0 240 Q300 252 520 264 V258 Q300 232 0 214 Z" fill="var(--ink)"/>
    </svg>
    <div class="wordmark">voltmere electrical</div>
    <div class="contact">
      <p class="contact-name">Dana Whitfield</p>
      <p class="contact-title">Portfolio Manager</p>
      <ul class="contact-list">
        <li>
          <svg class="contact-icon" viewBox="0 0 14 14" aria-hidden="true">
            <circle cx="7" cy="7" r="7" fill="var(--purple)"/>
            <rect x="4.5" y="3" width="5" height="8" rx="1" fill="none" stroke="#fff" stroke-width="1"/>
          </svg>
          (020) 555-0148
        </li>
        <li>
          <svg class="contact-icon" viewBox="0 0 14 14" aria-hidden="true">
            <circle cx="7" cy="7" r="7" fill="var(--purple)"/>
            <rect x="3.5" y="4.5" width="7" height="5" fill="none" stroke="#fff" stroke-width="1"/>
            <path d="M3.5 4.5 L7 7.5 L10.5 4.5" fill="none" stroke="#fff" stroke-width="1"/>
          </svg>
          hello@voltmere.com
        </li>
        <li>
          <svg class="contact-icon" viewBox="0 0 14 14" aria-hidden="true">
            <circle cx="7" cy="7" r="7" fill="var(--purple)"/>
            <circle cx="7" cy="7" r="3.6" fill="none" stroke="#fff" stroke-width="1"/>
            <path d="M3.4 7 H10.6 M7 3.4 V10.6" stroke="#fff" stroke-width="0.8"/>
          </svg>
          www.voltmere.com
        </li>
      </ul>
    </div>
    <p class="address">PO BOX 48, Harbour Road, Unit 4, Leeds</p>
  </section>

</body>
</html>
```